One Page Sales Flyer for Wireless Survey- Computer Hardware

I want a designer to create a one page 4 color sales slick to be given to our sales team to sell to the end customers. I would like a visual picture of a heat map so zavvix "heat map wireless" to get an idea of how that image should look.

```html
<!DOCTYPE html>
<html lang="en">
<head>
<meta charset="utf-8">
<title>LUMVEX – Wireless Site Survey</title>
<link href="https://fonts.googleapis.com/css2?family=Arimo:wght@400;700&display=swap" rel="stylesheet">
<style>
  :root {
    --blue: #1d14f0;
    --blue-light: #3b38f4;
    --yellow: #f7e300;
    --orange: #f6a61e;
    --black: #111111;
    --white: #ffffff;
    --sky: #4bb8ff;
    --heading: #f4e61a;
  }
  * { margin: 0; padding: 0; box-sizing: border-box; }
  html, body { width: 840px; height: 1200px; overflow: hidden; background: var(--blue); }
  .flyer {
    position: relative;
    width: 840px;
    height: 1200px;
    overflow: hidden;
    background: var(--blue);
    font-family: "Arimo", Arial, sans-serif;
    color: var(--white);
  }
  .backdrop { position: absolute; inset: 0; }
  .brand {
    position: absolute;
    left: 26px;
    top: 38px;
    display: flex;
    flex-direction: column;
    align-items: center;
    gap: 14px;
  }
  .brand-mark {
    width: 84px;
    height: 84px;
    background: var(--sky);
    border-radius: 10px;
  }
  .brand-name {
    font-size: 38px;
    font-weight: 400;
    letter-spacing: 2px;
    color: var(--white);
    line-height: 1;
  }
  .section-title {
    position: absolute;
    color: var(--heading);
    font-weight: 700;
    font-size: 15.5px;
    letter-spacing: 0.1px;
  }
  .section-body {
    position: absolute;
    font-weight: 700;
    font-size: 11px;
    line-height: 16px;
  }
  .what-title { left: 13px; top: 754px; }
  .what-body { left: 14px; top: 786px; width: 290px; }
  .need-title { left: 13px; top: 934px; }
  .need-body { left: 12px; top: 964px; width: 440px; font-size: 10.2px; line-height: 14.6px; }
  .why-title { left: 482px; top: 641px; font-size: 19.5px; }
  .why-body {
    position: absolute;
    left: 489px;
    top: 682px;
    font-weight: 700;
    font-size: 16px;
    line-height: 24.2px;
    white-space: pre;
  }
  .contact {
    position: absolute;
    left: 471px;
    top: 1138px;
    color: var(--black);
    font-weight: 700;
    font-size: 16px;
    line-height: 24px;
  }
</style>
</head>
<body>
<div class="flyer">
  <svg class="backdrop" width="840" height="1200" viewBox="0 0 840 1200">
    <defs>
      <linearGradient id="bandGlow" x1="0" y1="0" x2="1" y2="0">
        <stop offset="0" stop-color="#f6a61e"/>
        <stop offset="0.6" stop-color="#f8c21a"/>
        <stop offset="1" stop-color="#f7e300"/>
      </linearGradient>
      <linearGradient id="heatTones" x1="0" y1="0" x2="0" y2="1">
        <stop offset="0" stop-color="#8fe04a"/>
        <stop offset="0.14" stop-color="#e8e63a"/>
        <stop offset="0.3" stop-color="#f08a22"/>
        <stop offset="0.5" stop-color="#e33a12"/>
        <stop offset="1" stop-color="#d8290e"/>
      </linearGradient>
    </defs>
    <polygon points="420,0 840,0 840,85" fill="var(--blue-light)"/>
    <polygon points="60,214 840,80 840,152 620,172" fill="url(#bandGlow)"/>
    <polygon points="620,172 840,152 840,232" fill="var(--black)"/>
    <polygon class="heat-map" role="img" aria-label="World heat map showing wireless signal strength, green to red"
             points="0,210 840,180 840,552 240,594 0,480" fill="url(#heatTones)"/>
    <polygon points="0,476 240,594 0,540" fill="var(--black)"/>
    <polygon points="0,592 840,548 840,562 480,660 0,690" fill="url(#bandGlow)"/>
    <polygon points="0,688 560,605 0,740" fill="var(--black)"/>
    <polygon points="0,1020 430,1100 0,1185" fill="var(--blue-light)"/>
    <polygon points="0,1185 840,1038 840,1090 0,1200" fill="var(--black)"/>
    <polygon points="0,1200 840,1090 840,1200" fill="url(#bandGlow)"/>
  </svg>

  <div class="brand">
    <div class="brand-mark"></div>
    <div class="brand-name">LUMVEX</div>
  </div>

  <h2 class="section-title why-title">WHY SHOULD THEY USE YOU?</h2>
  <p class="why-body">42% of businesses report some
issues with wireless connectivity
and acknowledge its effect on
the bottom line*Most of these
problems are solved through
either fine tuning the current
equipment (managed services)
or purchasing new equipment
(incremental sales)
of which you can provide bothBeing
a one-stop shop for all your customer’s
IT needs prevents them from
needing additional vendorsThe
increase of IoT (Internet of things)
and BYOD (Bring Your Own Device</p>

  <h2 class="section-title what-title">WHAT IS A WIRELESS SITE SURVEY OR HEAT MAP?</h2>
  <p class="section-body what-body">A wireless site survey is a compilation of reports showing a visual representation of health of your wireless network. This does not only show how strong or weak a wireless signal is in any location it also helps aid in channel and placement to ensure maximum stable data rates are archived even where the single appears strong</p>

  <h2 class="section-title need-title">WHY DO CUSTOMERS NEED A SITE SURVEY?</h2>
  <p class="section-body need-body">Any variety of factors can contribute to an unhealthy wireless network (electrical, motors, materials used in construction, distance, neighboring wireless networks, etc.) and traditional methods that use only blueprints and a computer program to show signal strength have shown to be ineffective</p>

  <div class="contact">
    <div>www.lumvex.com info@lumvex.com</div>
    <div>555-014-2870</div>
  </div>
</div>
</body>
</html>
```